Design a modern business card

Hello!

We are looking for business card design.
We have a logo, color scheme, etc.. We want a modern design and that stands out and pops
NO GENERIC

See the EXAMPLES ATTACHED of my other business. I like this concept/modern idea and follow this IDEA

Design MUST include a SPOT UV MASK:
If you need info see: [login to view URL]
Size: 2" X 3.5"
We will PRINT THE CARD with SILK LAMINATION and SPOT UV MASK

On the FRONT I need the following:
LOGO: attached
Name: Mark Tellan
Phone Number: 417-862-0934
Title: Founder; CEO
Website: [login to view URL]

On the BACK I need the following:
ALSO add SMALL LOGO on the back in the background.. make the ENTIRE back scattered with small logo in the background

LOGO - make it large on the back.. it will be UV - see example Velvet Haze attached
Instagram: FitoVarda
Facebook: FitoVarda
SnapChat: FitoVarda
For Social media, use the icons for each of the social media..
#KeepClimbing
#FitoVarda
#ForgeYourFrame

Winner will provide:
AI/source file
JPG
JPG of mock

Final submission will also do JPG and AI using the real name and details for 3 employees
Basically I will tell the winner the 3 names of our employees and you will put that in the card, send us the AI and JPG

```html
<!DOCTYPE html>
<html lang="en">
<head>
<meta charset="utf-8">
<title>FitoVarda Business Card</title>
<link rel="stylesheet" href="https://fonts.googleapis.com/css2?family=Archivo:wght@700;800&family=Michroma&display=swap">
<style>
  :root {
    --stage: #5f5f5f;
    --brand-red: #d71300;
    --card-white: #ffffff;
    --ink: #231f20;
    --band-red: #d7150a;
  }
  * { margin: 0; padding: 0; box-sizing: border-box; }
  html, body {
    width: 1200px;
    height: 1173px;
    overflow: hidden;
    background: var(--stage);
  }
  .stage {
    position: relative;
    width: 1200px;
    height: 1173px;
  }
  .card {
    position: absolute;
    left: 267px;
    width: 666px;
    height: 381px;
    box-shadow: 0 2px 6px rgba(0,0,0,0.25);
  }
  .card-back {
    top: 156px;
    background: var(--brand-red);
    border-radius: 60px 0 60px 0;
    overflow: hidden;
  }
  .logo-pattern {
    position: absolute;
    inset: 0;
    background: linear-gradient(180deg, #db1a06 0%, #d31200 100%);
  }
  .back-wordmark {
    position: absolute;
    left: 0;
    right: 0;
    top: 158px;
    text-align: center;
    font-family: "Michroma", sans-serif;
    font-size: 44px;
    color: #ffffff;
    letter-spacing: 2px;
  }
  .card-front {
    top: 640px;
    background: var(--card-white);
    border-radius: 0 60px 0 60px;
  }
  .front-wordmark {
    position: absolute;
    right: 30px;
    top: 40px;
    font-family: "Michroma", sans-serif;
    font-size: 19px;
    letter-spacing: 9px;
    color: var(--ink);
    text-transform: lowercase;
  }
  .social-row {
    position: absolute;
    right: 33px;
    top: 77px;
    display: flex;
    gap: 14px;
  }
  .social-row span {
    width: 23px;
    height: 23px;
    background: var(--ink);
    border-radius: 3px;
  }
  .name-band {
    position: absolute;
    left: 0;
    top: 152px;
    width: 280px;
    height: 38px;
    background: var(--band-red);
  }
  .person-name {
    position: absolute;
    left: 36px;
    top: 152px;
    line-height: 38px;
    font-family: "Archivo", sans-serif;
    font-weight: 800;
    font-size: 31px;
    color: #ffffff;
  }
  .person-title {
    position: absolute;
    left: 34px;
    top: 197px;
    font-family: "Archivo", sans-serif;
    font-weight: 700;
    font-size: 25px;
    color: var(--ink);
  }
  .person-phone {
    position: absolute;
    left: 34px;
    top: 233px;
    display: flex;
    align-items: center;
    gap: 4px;
    font-family: "Archivo", sans-serif;
    font-weight: 700;
    font-size: 22px;
    color: var(--ink);
  }
  .website {
    position: absolute;
    left: 0;
    right: 0;
    top: 337px;
    text-align: center;
    font-family: "Michroma", sans-serif;
    font-size: 15px;
    letter-spacing: 4px;
    color: var(--ink);
    padding-left: 10px;
  }
</style>
</head>
<body>
<main class="stage">
  <section class="card card-back">
    <div class="logo-pattern" role="img" aria-label="Faint repeating pattern of small brand marks and wordmarks across the red card"></div>
    <div class="back-wordmark">FitoVarda</div>
  </section>

  <section class="card card-front">
    <div class="front-wordmark">fitovarda</div>
    <div class="social-row" aria-label="Social media">
      <span></span><span></span><span></span>
    </div>
    <div class="name-band"></div>
    <div class="person-name">MARK TELLAN</div>
    <div class="person-title">Founder / CEO</div>
    <div class="person-phone">
      <svg width="24" height="24" viewBox="0 0 24 24" aria-hidden="true">
        <rect x="0" y="0" width="24" height="24" rx="4" fill="#231f20"/>
        <path d="M7.5 5.5c.6-.4 1.3-.3 1.7.3l1.3 2c.3.5.2 1.2-.2 1.6l-.9.8c.6 1.5 1.9 2.9 3.4 3.6l.8-.9c.4-.5 1.1-.6 1.6-.2l2 1.3c.6.4.7 1.1.3 1.7l-.8 1.1c-.6.8-1.7 1.1-2.7.7-3.4-1.3-6.1-4-7.4-7.4-.4-1 0-2.1.7-2.7z" fill="#ffffff"/>
      </svg>
      <span>417-862-0934</span>
    </div>
    <div class="website">www.fitovarda.com</div>
  </section>
</main>
</body>
</html>
```